Design and put together a 5 page A4 brochure for a Training Programme

Harrowgate College of Learning deliver a Nationally Accredited Programme in Medical Reception and Administration.

We have a new Qualification (Cert III Business Administration) and we require a 5 page brochure to be designed. (I have CHANGED THIS TO 5 Pages as I can see it is too crowded and not clean enough)

I would put a 6th page in as an application form.

We have recently rebranded our website which is currently under development - so a .jpg will be available of the 'look and feel of this'. I will also upload some stock photos which could be used in the design.

This is an important project for us - so your fantastic work will be greatly appreciated.

This project is fairly urgent - so it is likely we will be choosing a 'winner' to work with sooner rather than later.

Thanks for considering!

I will be uploading various graphics/drafts now.
Updates

Project Deadline Extended Reason: I need a bit longer perhaps than Wednesday but will most likely be closing this early - either Wed or Thur. Your earliest designs would be most appreciated! Added Monday, July 18, 2016

Target Market(s)

1/ Women 25-45 yrs undertaking studies in being a medical receptionist
2/ Medical Practices who are hiring Trainees for their medical clinic or hospital

Industry/Entity Type

Medical

Font styles to use
Serif
Sans Serif

Colors
0455a3
fbe7d2
f68e4e
fef4ee
3176b5
33a6d7
f37122

Requirements
Must have
• Clear and clean design - professional
• Graphics of medical pictures (I will supply some so you get the look and feel of wht we are looking for)
• Corporate branding (I will upload a .jpg of new website design for look and feel
• The colour I would like with blue is also a STONE colour - I could not find it in the colour wheel on this site.
• The partner logos should be on the last page probably in one faded colour (such as grey)
Should not have
• I must be able to see the inside of the brochure also, I can not pick this purely on the front cover. Thanks :-)
• I have also now updated the Company Logo

```html
<!DOCTYPE html>
<html lang="en">
<head>
<meta charset="utf-8">
<title>Course Outline and Course Content spread</title>
<link href="https://fonts.googleapis.com/css2?family=Comfortaa:wght@400;700&family=Open+Sans:wght@400;600&display=swap" rel="stylesheet">
<style>
:root{
  --blue:#3176b5;
  --sky:#33a6d7;
  --navy:#0455a3;
  --ink:#4a4d52;
  --muted:#7c8087;
  --dark:#3c3f44;
  --cell:#e4e4ee;
  --rule:#c9cbd2;
  --stage:#dcdcd8;
  --paper:#ffffff;
}
*{box-sizing:border-box;margin:0;padding:0}
html,body{width:1200px;height:804px;overflow:hidden;background:var(--stage)}
body{font-family:"Open Sans",Arial,sans-serif;color:var(--ink);position:relative}
.spread{position:absolute;left:48px;top:12px;width:1104px;height:780px;display:flex;box-shadow:0 6px 18px rgba(0,0,0,.18)}
.page{position:relative;width:552px;height:780px;overflow:hidden;background:var(--paper)}
.heading{font-family:"Comfortaa",Arial,sans-serif;font-weight:700;font-size:30px;color:var(--dark)}
.heading .accent{color:var(--blue)}

/* left page */
.photo{position:absolute;inset:0;background:linear-gradient(160deg,#eef0f2 0%,#d6dade 30%,#b9c6cf 55%,#6aa7cf 80%,#cfd6dc 100%)}
.quote{position:absolute;left:60px;top:40px;width:400px;font-size:8.5px;line-height:1.45;color:var(--muted)}
.quote .mark{position:absolute;font-family:"Comfortaa",sans-serif;font-weight:700;font-size:46px;color:var(--sky);line-height:1}
.quote .open{left:-34px;top:-6px}
.quote .close{right:-34px;top:14px}
.quote .author{display:block;text-align:right;margin-top:8px}
.outline{position:absolute;left:70px;top:420px;width:440px;height:340px;background:rgba(255,255,255,.72);border-radius:22px;padding:28px 30px 20px}
.outline .heading{border-bottom:2px solid var(--blue);padding-bottom:4px;margin-bottom:12px;width:340px}
.outline p{font-size:7.6px;line-height:1.5;margin-bottom:8px;color:var(--ink)}
.outline p.lead{color:var(--blue);border-top:1px solid var(--rule);padding-top:10px;margin-top:4px}

/* right page */
.topline{position:absolute;left:20px;top:54px;width:300px;height:2px;background:var(--blue)}
.brand{position:absolute;left:330px;top:38px;display:flex;align-items:center;gap:6px;font-size:8px;font-weight:600;color:var(--dark);white-space:nowrap}
.brand .dot{width:12px;height:12px;border-radius:50%;background:var(--navy);flex:none}
.tab{position:absolute;right:0;top:34px;width:60px;height:20px;background:var(--dark)}
.tab .arrow{position:absolute;left:0;top:0;width:24px;height:20px;background:var(--sky);display:flex;align-items:center;justify-content:center}
.content{position:absolute;left:44px;top:76px;width:460px}
.sub{font-size:9px;color:var(--muted);margin:4px 0 18px}
.section{display:flex;margin-bottom:12px}
.section .label{width:130px;font-family:"Comfortaa",sans-serif;font-weight:700;font-size:11px;color:var(--sky);padding-top:10px}
.section.wide{flex-direction:column}
.section.wide .label{width:auto;padding:0 0 4px 0}
.units{flex:1;border-left:1px solid var(--rule);border-bottom:1px solid var(--rule)}
.unit{display:flex;font-size:8px;min-height:16px;border-top:1px solid var(--rule)}
.unit .code{width:90px;text-align:right;padding:3px 6px;color:var(--muted)}
.unit .desc{flex:1;background:var(--cell);padding:3px 8px;color:var(--ink);display:flex;align-items:center;border-right:1px solid var(--rule)}
.unit .desc.empty{background:none;border-right:none}
.section.wide .units{margin-left:40px}
.bonus h3{font-family:"Comfortaa",sans-serif;font-weight:700;font-size:12px;color:var(--sky);margin:6px 0 6px}
.bonus li{list-style:none;font-size:8px;display:flex;align-items:center;gap:5px;margin-bottom:2px}
.bonus svg{flex:none}
.footer{position:absolute;left:0;bottom:0;width:100%;height:34px;background:var(--dark);display:flex;align-items:center}
.pagenum{width:20px;height:20px;border-radius:50%;border:2px solid #fff;background:var(--navy);color:#fff;font-size:9px;font-weight:600;display:flex;align-items:center;justify-content:center;margin-left:22px}
.url{flex:1;text-align:center;color:#fff;font-size:9px}
.social{width:140px;height:44px;align-self:flex-end;background:var(--blue);display:flex;align-items:center;justify-content:center;gap:8px}
.social span{width:11px;height:11px;background:#fff;border-radius:2px}
</style>
</head>
<body>
<div class="spread">
  <section class="page page-outline">
    <div class="photo" role="img" aria-label="Photo of two smiling medical staff, a doctor in a white coat and a nurse in blue scrubs, in a bright hospital corridor"></div>
    <blockquote class="quote">
      <span class="mark open">&ldquo;</span>
      The trainers were excellent in their delivery and knowledge. I want to say a huge thank you to Harrowgate for the course and knowledge I came away with. I have secured a fantastic job after my first application! Such good value for money too! I would highly recommend it. I'm a mature age person so it's never too late to up-skill yourself to get what you deserve!
      <span class="mark close">&rdquo;</span>
      <span class="author">- Joan Whitby</span>
    </blockquote>
    <div class="outline">
      <h2 class="heading"><span class="accent">Course</span> Outline</h2>
      <p>Gain the knowledge and skills to become a professional Medical Administrator by completing the Nationally Recognised Qualification in Business Administration (Medical). You will be employed in a variety of professional environments where your skills and contribution will be highly valued.</p>
      <p>This qualification is designed to give you the knowledge and skills required to become an integral part of the medical healthcare team. Find yourself in a role where you're appreciated by patients and your support is relied upon by the clinical team to keep the business administration running smoothly.</p>
      <p>Your efficient, diligent, caring approach makes a significant difference to the lives of others and engenders a sense of job satisfaction second to none.</p>
      <p>Medical Administration is a vibrant career with qualified administrators being widely sought after in industry, therefore career opportunities are strong. With an aging population, medical administration is a government recognised growth area with strong upwards projections of job opportunities predicted into 2020 and beyond.</p>
      <p>There are a variety of opportunities in diverse fields such as general practice, specialist practice, hospitals, dental and allied health. For students interested in career advancement, there are strong pathways to promotion available into more senior levels of administration and practice management.</p>
      <p class="lead">This course is ideal for those wanting to begin a career in the health professions and for workplace trainees. Mature aged students are also highly sought after in the medical space. Career opportunities are high for both part-time and full-time employees.</p>
    </div>
  </section>

  <section class="page page-content">
    <div class="topline"></div>
    <div class="brand"><span class="dot"></span>Harrowgate College of Learning</div>
    <div class="tab"><span class="arrow"><svg width="10" height="10" viewBox="0 0 10 10"><circle cx="5" cy="5" r="4.5" fill="#fff"/><path d="M6 2.5 3.5 5 6 7.5" stroke="#33a6d7" stroke-width="1.4" fill="none"/></svg></span></div>

    <div class="content">
      <h2 class="heading"><span class="accent">Course</span> Content</h2>
      <p class="sub">Units of Competency Covered in the Harrowgate Programme :</p>

      <div class="section">
        <div class="label">Core</div>
        <div class="units">
          <div class="unit"><span class="code">BSBITU307</span><span class="desc">Develop keyboarding speed and accuracy</span></div>
          <div class="unit"><span class="code">BSBWHS201</span><span class="desc">Contribute to health and safety of self and others</span></div>
          <div class="unit"><span class="code"></span><span class="desc empty"></span></div>
        </div>
      </div>

      <div class="section">
        <div class="label">Medical Skill Set</div>
        <div class="units">
          <div class="unit"><span class="code">BSBMED301</span><span class="desc">Interpret and apply medical terminology appropriately</span></div>
          <div class="unit"><span class="code">BSBMED302</span><span class="desc">Prepare and process medical accounts</span></div>
          <div class="unit"><span class="code">BSBMED303</span><span class="desc">Maintain patient records</span></div>
          <div class="unit"><span class="code">BSBMED305</span><span class="desc">Apply the principles of confidentiality, privacy and security within the medical environment</span></div>
          <div class="unit"><span class="code">BSBMED304</span><span class="desc">Assist in controlling stocks and supplies</span></div>
          <div class="unit"><span class="code"></span><span class="desc empty"></span></div>
        </div>
      </div>

      <div class="section wide">
        <div class="label">Business Administration (Medical) Skill Set including an introduction to Audio-typing</div>
        <div class="units">
          <div class="unit"><span class="code">BSBITU309</span><span class="desc">Produce desktop published documents</span></div>
          <div class="unit"><span class="code">BSBITU303</span><span class="desc">Design and produce text documents</span></div>
          <div class="unit"><span class="code">BSBITU306</span><span class="desc">Design and produce business documents</span></div>
          <div class="unit"><span class="code">BSBWRT301</span><span class="desc">Write simple documents</span></div>
          <div class="unit"><span class="code">BSBADM303</span><span class="desc">Produce texts from audio transcription</span></div>
          <div class="unit"><span class="code"></span><span class="desc empty"></span></div>
        </div>
      </div>

      <div class="section wide">
        <div class="label">Customer Service for Medical Administrators</div>
        <div class="units">
          <div class="unit"><span class="code">BSBCUS301</span><span class="desc">Deliver and monitor a service to customers</span></div>
          <div class="unit"><span class="code"></span><span class="desc empty"></span></div>
        </div>
      </div>

      <div class="bonus">
        <h3>Bonus training offered as part of the Harrowgate Programme</h3>
        <ul>
          <li><svg width="9" height="9" viewBox="0 0 9 9"><rect x=".5" y=".5" width="8" height="8" fill="none" stroke="#4a4d52"/><path d="M2 4.5 4 6.5 7.5 2" stroke="#4a4d52" stroke-width="1.3" fill="none"/></svg>Medical Triage for Non-Clinical Staff and Customer Service (BSBCUS301)</li>
          <li><svg width="9" height="9" viewBox="0 0 9 9"><rect x=".5" y=".5" width="8" height="8" fill="none" stroke="#4a4d52"/><path d="M2 4.5 4 6.5 7.5 2" stroke="#4a4d52" stroke-width="1.3" fill="none"/></svg>CPR First Aid Qualification with National First Aid Council (BSBSXXXXXX)</li>
          <li><svg width="9" height="9" viewBox="0 0 9 9"><rect x=".5" y=".5" width="8" height="8" fill="none" stroke="#4a4d52"/><path d="M2 4.5 4 6.5 7.5 2" stroke="#4a4d52" stroke-width="1.3" fill="none"/></svg>DocuWrite 2010 Essentials Short Course</li>
          <li><svg width="9" height="9" viewBox="0 0 9 9"><rect x=".5" y=".5" width="8" height="8" fill="none" stroke="#4a4d52"/><path d="M2 4.5 4 6.5 7.5 2" stroke="#4a4d52" stroke-width="1.3" fill="none"/></svg>PageCraft 2010 Essentials Short Course</li>
          <li><svg width="9" height="9" viewBox="0 0 9 9"><rect x=".5" y=".5" width="8" height="8" fill="none" stroke="#4a4d52"/><path d="M2 4.5 4 6.5 7.5 2" stroke="#4a4d52" stroke-width="1.3" fill="none"/></svg>Harrowgate KeyPace Online Keyboard Programme and certification to Australian Standards</li>
        </ul>
      </div>
    </div>

    <footer class="footer">
      <span class="pagenum">11</span>
      <span class="url">www.harrowgatelearning.edu.au</span>
      <div class="social"><span></span><span></span><span></span><span></span></div>
    </footer>
  </section>
</div>
</body>
</html>
```